Drink Product Brochure

We have 3 tea drinks in plastic bottles that we'd like to put in a brochure (8"x11" sheet) and focus on all natural, no preservatives, and supporting a nonprofit orphanage. The logo boasts a one color design - green. The brochure should make 3-4 key highlights, and allow at least one section product overview. Clean, modern design with not to many distractions but an inviting natural look and highlight the key features.

Target Market(s)

Middle age

Font styles to use
Serif
Sans Serif

Colors
add136
85cae6
b768aa

```html
<!DOCTYPE html>
<html lang="en">
<head>
<meta charset="utf-8">
<title>Verdant Leaf Tea – Trifold Brochure</title>
<link rel="stylesheet" href="https://fonts.googleapis.com/css2?family=Open+Sans:wght@400;600;700;800&family=Parisienne&display=swap">
<style>
  :root {
    --canvas: #e4e4e4;
    --paper: #ffffff;
    --green: #3f8f36;
    --green-dark: #1f6b22;
    --green-deep: #17591b;
    --lime: #add136;
    --lime-soft: #c8e27a;
    --ink: #1d1d1d;
    --ink-soft: #555555;
    --sky: #85cae6;
    --berry: #b768aa;
  }
  * { box-sizing: border-box; margin: 0; padding: 0; }
  html, body {
    width: 1200px; height: 800px; overflow: hidden;
    background: var(--canvas);
    font-family: "Open Sans", Arial, sans-serif;
  }
  .brochure {
    position: absolute; left: 90px; top: 20px;
    width: 1020px; height: 760px;
    box-shadow: 0 10px 30px rgba(0,0,0,.18);
    background: var(--paper);
  }
  .brochure-bg { position: absolute; inset: 0; }
  .panel { position: absolute; top: 0; width: 340px; height: 760px; }
  .panel--about { left: 0; }
  .panel--contact { left: 340px; }
  .panel--cover { left: 680px; }

  .brand {
    position: absolute; display: flex; align-items: center; gap: 8px;
    color: var(--green); font-weight: 800; font-size: 22px; letter-spacing: .5px;
    text-transform: uppercase; line-height: 1;
  }
  .brand-mark { width: 16px; height: 16px; background: var(--green); }
  .panel--about .brand { left: 0; right: 0; top: 55px; justify-content: center; }
  .panel--cover .brand { left: 0; right: 0; top: 40px; justify-content: center; }

  .photo { position: absolute; }
  .photo--bottles {
    left: 45px; top: 120px; width: 150px; height: 270px; border-radius: 10px;
    background: linear-gradient(90deg, #e0563d 0%, #f29a3a 50%, #9bc24a 100%);
    opacity: .9;
  }
  .photo--iced-tea {
    left: 0; top: 140px; width: 340px; height: 260px;
    background: linear-gradient(160deg, #e8eef2 0%, #b38a4a 45%, #c25072 70%, #e0a63a 100%);
  }

  .tag {
    position: absolute; color: #fff; background: var(--green);
    font-weight: 600; font-size: 13px; padding: 5px 14px;
    transform: rotate(-18deg); white-space: nowrap;
    border-radius: 3px;
  }
  .tag--natural { left: 205px; top: 228px; }
  .tag--preserv { left: 198px; top: 275px; }

  .section-title { color: #fff; font-weight: 700; font-size: 15px; }
  .body-copy { color: #fff; font-size: 10.5px; line-height: 15px; }
  .about { position: absolute; left: 28px; right: 28px; top: 462px; }
  .about .body-copy { margin: 5px 0 9px; }
  .about .section-title + .body-copy + .body-copy { margin-bottom: 12px; }

  .web-pill {
    position: absolute; left: 40px; right: 40px; height: 30px;
    border-radius: 15px;
    background: linear-gradient(180deg, var(--lime-soft) 0%, var(--lime) 55%, #86b12a 100%);
    color: var(--green-deep); font-size: 15px; font-weight: 400;
    display: flex; align-items: center; justify-content: center;
  }
  .web-pill b { font-weight: 800; }
  .panel--about .web-pill { bottom: 24px; }
  .panel--contact .web-pill { bottom: 24px; }
  .panel--cover .web-pill { top: 566px; }

  .intro { position: absolute; left: 40px; right: 40px; top: 60px; text-align: center; }
  .intro .body-copy { margin-bottom: 18px; }

  .contact {
    position: absolute; left: 30px; right: 30px; top: 430px;
    text-align: center; color: #fff;
  }
  .contact .section-title { font-weight: 400; font-size: 17px; margin-bottom: 10px; }
  .contact-icon { display: block; margin: 6px auto 3px; width: 14px; height: 14px; }
  .contact-line { font-size: 11.5px; font-weight: 600; line-height: 15px; }
  .contact-line--email { font-size: 13px; font-weight: 700; }

  .claims {
    position: absolute; left: 0; right: 0; top: 108px; height: 26px;
    background: var(--green); color: #fff;
    font-size: 11px; font-weight: 700; letter-spacing: .5px;
    display: flex; align-items: center; padding-left: 20px;
    border-bottom: 3px solid var(--lime);
  }
  .cover-headline {
    position: absolute; left: 0; right: 0; top: 462px; text-align: center;
  }
  .cover-script {
    font-family: "Parisienne", cursive; color: var(--green);
    font-size: 46px; line-height: 1;
  }
  .cover-sub {
    margin-top: 6px; color: var(--ink); font-weight: 800; font-size: 19px; letter-spacing: .5px;
  }
</style>
</head>
<body>
<main class="brochure">
  <svg class="brochure-bg" viewBox="0 0 1020 760" width="1020" height="760" aria-hidden="true">
    <rect x="0" y="0" width="1020" height="760" fill="var(--paper)"/>
    <!-- about panel wave -->
    <path d="M0 430 C110 395 230 440 340 372 L340 390 C230 460 110 420 0 455Z" fill="var(--lime)"/>
    <path d="M0 455 C110 420 230 460 340 390 L340 404 C230 476 110 438 0 470Z" fill="var(--green-dark)"/>
    <path d="M0 470 C110 438 230 476 340 404 L340 760 L0 760Z" fill="var(--green)"/>
    <!-- contact panel -->
    <rect x="340" y="0" width="340" height="760" fill="var(--green)"/>
    <path d="M340 372 C450 340 560 365 680 330 L680 348 C560 385 450 362 340 392Z" fill="var(--lime)"/>
    <path d="M340 392 C450 362 560 385 680 348 L680 372 C560 410 450 390 340 410Z" fill="var(--green-dark)"/>
    <!-- cover panel wave -->
    <path d="M680 420 C790 395 900 430 1020 388 L1020 400 C900 446 790 414 680 436Z" fill="var(--green-dark)"/>
    <path d="M680 440 C790 420 900 450 1020 410 L1020 416 C900 458 790 428 680 446Z" fill="var(--lime)"/>
    <!-- folds -->
    <line x1="340" y1="0" x2="340" y2="760" stroke="rgba(0,0,0,.12)" stroke-width="1"/>
    <line x1="680" y1="0" x2="680" y2="760" stroke="rgba(0,0,0,.12)" stroke-width="1"/>
  </svg>

  <section class="panel panel--about">
    <div class="brand"><span class="brand-mark"></span>Verdant Leaf Tea</div>
    <div class="photo photo--bottles" role="img" aria-label="Three bottles of fruit tea drinks"></div>
    <span class="tag tag--natural">All Natural</span>
    <span class="tag tag--preserv">No Preservatives</span>
    <div class="about">
      <h2 class="section-title">About us</h2>
      <p class="body-copy">Sed ut perspiciatis unde omnis iste natus error sit voluptatem accusantium doloremque laudantium, totam rem aperiam, eaque ipsa quae ab illo inventore veritatis et quasi architecto beatae vitae dicta sunt explicabo.</p>
      <p class="body-copy">Nemo enim ipsam voluptatem quia voluptas sit aspernatur aut odit aut fugit, sed quia consequuntur magni dolores eos qui ratione voluptatem sequi nesciunt. Neque porro quisquam est, qui dolorem ipsum quia dolor sit amet, consectetur.</p>
      <h2 class="section-title">Supporting Nonprofit Orphanage</h2>
      <p class="body-copy">Ut enim ad minima veniam, quis nostrum exercitationem ullam corporis suscipit laboriosam</p>
    </div>
    <div class="web-pill">www.<b>verdantleaftea</b>.com</div>
  </section>

  <section class="panel panel--contact">
    <div class="intro">
      <p class="body-copy">Lorem ipsum dolor sit amet, consectetur adipiscing elit. Etiam dapibus laoreet eleifend. Suspendisse lobortis tellus massa. Donec nec commodo ipsum. Praesent mollis vitae leo eget feugiat. Donec vitae aliquet est, ut semper lectus. Pellentesque risus elit, vehicula faucibus nibh ac, egestas pharetra ipsum. Aenean euismod malesuada sollicitudin.</p>
      <p class="body-copy">Lorem ipsum dolor sit amet, consectetur adipiscing elit. Etiam dapibus laoreet eleifend. Suspendisse lobortis tellus massa. Donec nec commodo ipsum. Praesent mollis vitae leo eget feugiat.</p>
    </div>
    <address class="contact" style="font-style:normal">
      <h2 class="section-title">Get in touch</h2>
      <svg class="contact-icon" viewBox="0 0 14 14" aria-hidden="true"><path d="M7 13 C3 8 2.5 6.5 2.5 5 A4.5 4.5 0 0 1 11.5 5 C11.5 6.5 11 8 7 13Z" fill="none" stroke="#fff" stroke-width="1.2"/><circle cx="7" cy="5" r="1.5" fill="#fff"/></svg>
      <p class="contact-line">1482 Willow Creek Rd, #210,<br>Suite B4, Austin, TX 78745</p>
      <svg class="contact-icon" viewBox="0 0 14 14" aria-hidden="true"><path d="M3 1.5 L5.5 1.5 L6.5 4.5 L5 5.5 C5.8 7.3 6.7 8.2 8.5 9 L9.5 7.5 L12.5 8.5 L12.5 11 C12.5 12 11.5 12.5 10.5 12.5 C5.5 12 2 8.5 1.5 3.5 C1.5 2.5 2 1.5 3 1.5Z" fill="none" stroke="#fff" stroke-width="1.1"/></svg>
      <p class="contact-line">(512) 555-0187</p>
      <svg class="contact-icon" viewBox="0 0 14 14" aria-hidden="true"><rect x="4" y="1.5" width="6" height="4" fill="#fff"/><rect x="1.5" y="5.5" width="11" height="5" rx="1" fill="#fff"/><rect x="4" y="9" width="6" height="4" fill="#fff" stroke="var(--green)" stroke-width="1"/></svg>
      <p class="contact-line">(512) 555-0192</p>
      <svg class="contact-icon" viewBox="0 0 14 14" aria-hidden="true"><rect x="1.5" y="3" width="11" height="8" fill="none" stroke="#fff" stroke-width="1.1"/><path d="M1.5 3 L7 8 L12.5 3" fill="none" stroke="#fff" stroke-width="1.1"/></svg>
      <p class="contact-line contact-line--email">hello@verdantleaftea.com</p>
    </address>
    <div class="web-pill">www.<b>verdantleaftea</b>.com</div>
  </section>

  <section class="panel panel--cover">
    <div class="brand"><span class="brand-mark"></span>Verdant Leaf Tea</div>
    <div class="claims">ALL NATURAL &nbsp;|&nbsp; NO PRESERVATIVES</div>
    <div class="photo photo--iced-tea" role="img" aria-label="Glasses of iced tea with lemon beside three bottles of tea drinks"></div>
    <div class="cover-headline">
      <p class="cover-script">Refreshing</p>
      <p class="cover-sub">YOUR SOUL AND MIND</p>
    </div>
    <div class="web-pill">www.<b>verdantleaftea</b>.com</div>
  </section>
</main>
</body>
</html>
```